Major Australian Food and Wine Event Web Design Project

The project will consist of 3 designs
The homepage
A city hub page
A general content page

The main audience who will visit the website will be (in Order of importance:

1) Visitors
- Mainly women 24 – 54 years (they are the main ticket buyers)
- In a relationship – so will go to the show with their partner
- In a good paying job or home maker – and who have disposable income to spend $30 a ticker
- Enjoy food, wine and going out
- Looking for a fun day out – although an event that is about food and wine – it is an event that most people will go to and have a fun day out – not too pretentious

A smaller proportion of the audience will be:
2) Exhibitors & sponsors ( both prospective and existing)
3) Media

Objectives:

- Functionality on home page and sub pages needs to be updated, clear, easy to navigate and inject a sense of ‘fun’ – need to make it look more professional
- Need to incorporate the many things that need to be on the home page and sub pages in a visually appealing manner
- Ensure the ‘Cons’ above are considered and reflected in functionality and design
- To not be too focus on the colours (these can be changed) – but focus on the functionality and overall design opportunities.

Approach:

Keywords to describe the Bright Plate & Vine Fair:
Fun day out, discover, learn, indulge, entertaining

Other website examples:

Some great consumers event websites from the UK really make our website look basic and juvenile – and below are some examples of the presentation of how we would like our website to look like:

http://www.morselfairs-example.com/london/ This website is clean, includes good social media integration and exudes a sense of fun. Their content pages, such as the features landing page also presents options in a clear and visually appealing way with a series of boxes including image and text http://www.morselfairs-example.com/london/content/343/Features

http://www.homecraftexpo-example.com/ - this is also a great website – and it incorporates all the elements we would be looking for on our homepage – but the background/skin also includes a sense of fun and cheekiness. Subpages also are consistent.

Features

• Its a fun day that offers great value for money
• Caters to all visitors, regardless of different levels of knowledge or interest in food, wine and cooking.
• Sample great quality food and wine products from hundreds of reputable exhibitors
• Learn more through many of the shows feature activities (Celeb Theatre, Wine Theatre, Cooking & Cheese Classes)

Functionality & Structure:

In a user friendly, easy to view way, we need to incorporate the following functionality elements on home page:
- main header (that will incorporate our current creative) with a ‘fun’ skin
- navigation tabs/references (hone, location, tickets, blog, sign up, exhibitors)
- navigation/content banner (rotating)
- Area for small intro about the show
- News and highlight section
- New exhibitors section
- Obvious Ticket call to action
- Obvious sign up call to action
- Social media buttons or links ( really like the moving gifs on the Homecraftexpo-example.com site
- area for advertising (MREC size) to sell to exhibitors/sponsors
- Show dates for all 5 shows (maybe in main header)

Subpage layout is also important and needs to reflect the homepage – so would also like to see examples of how this would look and tie in with navigation – we generally have a lot of content on these pages, so clear navigation would be useful. – see below for further details of functionality for city Hubs

‘CITY HUB’ BRIEF
When navigating to each location the user will be taken to a ‘CITY HUB’ which should replicate design and content elements of a main HOME page, as well as reflect more specific information for each Show. Elements which must appear on this page are:
• FEATURES – which may be displayed in categories (in boxes, see appendix 1.0) which will link through to relevant content pages. Or in one box which will link through to a features page with all presented in boxes
• CHEFS – may be displayed as a separate icon box which will link to chefs page with bios, Celeb Theatre timetable etc.
• TICKETS – either a button or clear callout to purchase tickets
• PLAN YOUR DAY – may be displayed in a separate content box which will then link through to getting there, sample itineraries and downloadable pocket show guide for visitors to print before coming to the Show.
• WHO’S EXHIBITING – to link back to city specific exhibitor lists

Our current website is out of date and has the following inadequacies (www.brightplatefair-example.com.au) -

The homepage
A city hub page
A general content page

1) Visitors

3) Media

Objectives:

Approach:

To be perceived as a fun, entertaining event with something for everyone - website creative and navigation must reflect this.

Other website examples:

Features

- New exhibitors section

‘CITY HUB’ BRIEF

- Dated design/layout
- Homepage too text heavy
- No content boxes that can be used for different features/areas (eg. News, Exhibitors etc)
- Uninspiring colours and skin(eg. grey background), does not reflect ‘a fun day out’
- Limited presence of social media platforms and lacks ‘community’
- No continuity in sub pages
- main banner too big – takes up too much space on homepage

Requirements
Must have
• As per above brief.

In addition:
Floating social media buttons on side
Wrap around image
Drop down menu (specifically for the location nav item)

```html
<!DOCTYPE html>
<html lang="en">
<head>
<meta charset="utf-8">
<title>Bright Plate &amp; Vine Fair</title>
<link href="https://fonts.googleapis.com/css2?family=Arvo:wght@400;700&family=Ubuntu:wght@500&family=Arimo:wght@400;700&family=Neucha&display=swap" rel="stylesheet">
<style>
:root{
  --navy:#262a63;
  --royal:#1a1a9c;
  --link:#1c1a8f;
  --purple:#5a3fb8;
  --purple-dark:#4a2fa6;
  --orange:#e8520f;
  --orange-light:#f59a3a;
  --hill:#7f9a78;
  --ink:#222;
  --muted:#999;
  --footer:#c1cde8;
  --slab:"Arvo",Georgia,serif;
  --sans:"Arimo",Arial,sans-serif;
  --head:"Ubuntu",Arial,sans-serif;
}
*{box-sizing:border-box;margin:0;padding:0}
html,body{width:870px;height:1200px;overflow:hidden}
body{position:relative;font-family:var(--sans);color:var(--ink);
  background:linear-gradient(180deg,#f3f4f2 0,#e6e8e4 560px,#a9b9a0 640px,var(--hill) 760px,#6f8a6b 1200px)}
.abs{position:absolute}
.topbar{left:0;top:0;width:870px;height:35px;background:linear-gradient(180deg,#33376f,var(--navy))}
.newsletter{left:418px;top:10px;color:#fff;font:700 11.5px var(--sans)}
.email{left:558px;top:5px;width:140px;height:22px;background:#fff;border:1px solid #ccc;font:10px var(--sans);color:#999;padding:5px 8px}
.signup-btn{left:699px;top:5px;width:44px;height:22px;background:#111;color:#fff;font:10.5px var(--sans);text-align:center;line-height:22px}
.logo-tab{left:75px;top:0;width:183px;height:184px}
.logo-name{left:88px;top:30px;width:158px;font:700 26px/1.15 var(--slab);color:var(--ink);text-align:center}
.nav{left:308px;top:124px;display:flex;font:13px var(--slab)}
.nav a{color:var(--royal);text-decoration:none;padding:3px 10px;margin-right:14px;text-shadow:1px 1px 0 #bbb}
.nav a.current{background:var(--royal);color:#fff;border-radius:3px;text-shadow:none}
.hero-photo{left:74px;top:187px;width:484px;height:231px;background:linear-gradient(120deg,#6d6d6d,#b5b1ab 55%,#d9d6d2)}
.hero-text{left:89px;top:200px;color:#fff;width:170px}
.hero-city{font:34px "Neucha",cursive;margin-bottom:10px}
.hero-text p{font:700 9px/1.3 var(--sans);margin-bottom:8px}
.hero-text .desc{font-weight:400}
.dots{left:424px;top:393px;display:flex;gap:2px}
.dots span{width:20px;height:17px;background:rgba(255,255,255,.7)}
.dots span:first-child{background:#5a4bb0}
.dates{left:558px;top:187px;width:205px;height:231px;background:linear-gradient(180deg,#fde7d6 0,#fcd7b9 55px,var(--orange-light) 80px,var(--orange) 230px)}
.dates h2{font:12px/1.3 var(--slab);color:var(--orange);padding:20px 0 6px 19px;width:185px;border-bottom:2px solid var(--orange)}
.dates-list{left:572px;top:284px;font:8.5px/1.65 var(--sans);color:#fff}
.dates-list b{display:inline-block;width:66px;font-weight:400}
.dates-list span{font:700 10.5px var(--slab)}
.book{left:583px;top:363px;width:162px;height:22px;background:var(--orange);border:1px solid #ffb37a;color:#fff;font:11px/20px var(--head);text-align:center;clip-path:polygon(0 0,94% 0,100% 50%,94% 100%,0 100%)}
.social{left:765px;top:223px;width:32px;height:163px;background:#fff;box-shadow:1px 1px 3px rgba(0,0,0,.3);padding:4px 5px}
.social span{display:block;width:22px;height:26px;margin-bottom:12px;background:#cfd4de;border-radius:3px}
.band{left:74px;top:423px;width:689px;height:115px;background:linear-gradient(180deg,var(--purple),var(--purple-dark));border:1px solid #7c67cc}
.feature{position:absolute;top:14px;width:155px;height:90px}
.feature .tile{position:absolute;left:0;top:0;width:40px;height:86px;border:2px solid #fff;border-radius:3px}
.feature h3{position:absolute;left:55px;top:3px;font:500 14px var(--head);color:#fff;white-space:nowrap}
.feature p{position:absolute;left:55px;top:24px;width:86px;font:8.5px/1.2 var(--sans);color:#fff}
.feature .more{position:absolute;left:50px;top:75px;width:84px;height:14px;background:#eef;border:1px solid #99a;font:700 8.5px/12px var(--sans);color:var(--link);text-align:center}
.main{left:74px;top:545px;width:689px;height:462px;background:#fff;box-shadow:0 0 3px rgba(0,0,0,.3)}
.title{left:85px;top:560px;width:462px;border-bottom:2px solid var(--royal);font:400 11.5px var(--slab);color:var(--royal);padding-bottom:3px}
.intro{left:87px;top:585px;width:455px;font:8.5px/1.35 var(--sans)}
.calendar{left:89px;top:624px}
.countdown{left:134px;top:630px;font:8.5px/1.4 var(--sans)}
.early{left:318px;top:630px;width:200px;height:22px;background:var(--orange);color:#fff;font:11px/22px var(--head);text-align:center;clip-path:polygon(0 0,95% 0,100% 50%,95% 100%,0 100%)}
.tabs{left:85px;top:686px;width:221px;border-bottom:2px solid var(--royal);display:flex}
.tabs span{font:11px/20px var(--sans);padding:0 9px;background:#ddd;color:#555}
.tabs span.on{background:var(--royal);color:#fff}
.col{width:220px}
.item-title{font:700 8.5px var(--sans);text-decoration:underline;color:var(--ink);margin-bottom:5px}
.item p{font:8.5px/1.35 var(--sans)}
.date{color:var(--muted)}
.news{left:86px;top:718px}
.news .item{margin-bottom:18px}
.feed-head{left:85px;top:860px;width:221px;border-bottom:2px solid var(--royal);font:10.5px var(--sans);color:var(--royal);display:flex;justify-content:space-between;padding-bottom:3px}
.feed-head span+span{color:#666}
.feed{left:86px;top:888px;width:220px}
.feed p{font:8.5px/1.4 var(--sans)}
.feed a,.feed b{color:var(--link);text-decoration:none}
.feed .ago{color:var(--muted);margin:3px 0 18px}
.ex-head{left:320px;top:684px;width:228px;border-top:2px solid #eee;border-bottom:2px solid var(--royal);font:10.5px/20px var(--sans);color:var(--royal);padding-left:1px}
.exhibitor{position:absolute;left:321px;width:228px}
.exhibitor .item-title{margin-bottom:6px}
.exhibitor p{width:135px;font:8.5px/1.3 var(--sans)}
.exhibitor .pic{position:absolute;left:152px;top:0;width:74px;height:72px}
.ad{left:571px;width:185px;background:#000;display:flex;align-items:center;justify-content:center;text-align:center;font:700 14px/1.15 var(--slab);color:#f5ec4a}
.ad-tall{top:560px;height:156px}
.ad-mid{top:723px;height:126px}
.ad-low{top:857px;height:125px}
.footer{left:74px;top:1013px;width:689px;height:159px;background:var(--footer);box-shadow:0 0 3px rgba(0,0,0,.3)}
.quick-head{left:86px;top:1024px;width:221px;border-bottom:2px solid var(--royal);font:700 10.5px var(--slab);color:var(--royal);padding-bottom:5px}
.quick{left:90px;top:1054px;display:grid;grid-template-columns:111px 110px;row-gap:2px;font:10px var(--slab)}
.quick a{color:var(--royal);text-decoration:none}
.foot-dates{left:317px;top:1013px;width:240px;height:144px;background:var(--orange)}
.foot-dates h2{font:400 11.5px var(--slab);color:#fff;padding:12px 13px 9px;border-bottom:2px solid #f5a070}
.foot-dates ul{list-style:none;padding:10px 13px;font:10.5px/1.6 var(--sans);color:#fff}
.foot-dates b{display:inline-block;width:83px;font-weight:400}
.foot-dates span{font:700 10.5px var(--slab)}
.foot-tab{left:644px;top:1013px;width:112px;height:112px}
.foot-name{left:652px;top:1030px;width:96px;font:700 14px/1.15 var(--slab);color:var(--ink);text-align:center}
.copyright{left:87px;top:1180px;font:700 8.5px var(--sans);color:#fff}
</style>
</head>
<body>
<div class="abs topbar"></div>
<div class="abs newsletter">Get newsletter updates</div>
<div class="abs email">Your email</div>
<div class="abs signup-btn">Sign up</div>

<svg class="abs logo-tab" viewBox="0 0 183 184" aria-hidden="true">
  <polygon points="0,0 183,0 183,184 91,160 0,184" fill="#fff" stroke="#ddd"/>
</svg>
<div class="abs logo-name">Bright Plate &amp; Vine Fair</div>

<nav class="abs nav">
  <a class="current">Home</a><a>Location</a><a>Tickets</a><a>Blog</a><a>Sign up</a><a>Exhibitors</a>
</nav>

<div class="abs hero-photo" role="img" aria-label="Photo of a chef drizzling sauce onto a plated dish"></div>
<div class="abs hero-text">
  <div class="hero-city">Sydney</div>
  <p>Sashimi Master class</p>
  <p>23rd June 2pm</p>
  <p class="desc">Neque porrp quisquam est qui dolorem ipsum quia dolor sit ...</p>
  <p>Read more &gt;</p>
</div>
<div class="abs dots"><span></span><span></span><span></span><span></span><span></span><span></span></div>

<div class="abs dates" role="img" aria-label="Orange hillside backdrop for the show dates">
  <h2>2012 Bright Plate &amp; Vine Fair Dates</h2>
</div>
<div class="abs dates-list">
  <div><b>SYDNEY</b><span>22nd-24th June</span></div>
  <div><b>MELBOURNE</b><span>22nd-24th July</span></div>
  <div><b>PERTH</b><span>22nd-24th August</span></div>
  <div><b>BRISBANE</b><span>22nd-24th September</span></div>
</div>
<div class="abs book">BOOK TICKETS NOW</div>

<div class="abs social" aria-label="Social links"><span></span><span></span><span></span><span></span></div>

<section class="abs band">
  <div class="feature" style="left:13px"><div class="tile" role="img" aria-label="Fish icon" style="background:#f58a2a"></div><h3>Chefs</h3><p>Neque porro quisquam est qui dolorem ipsum quia dolor sit...</p><div class="more">Read more &gt;</div></div>
  <div class="feature" style="left:181px"><div class="tile" role="img" aria-label="Coffee cup icon" style="background:#c3d44a"></div><h3>Plan your day</h3><p>Neque porro quisquam est qui dolorem ipsum quia dolor sit...</p><div class="more">Read more &gt;</div></div>
  <div class="feature" style="left:351px"><div class="tile" role="img" aria-label="Cocktail glass icon" style="background:#e4e04a"></div><h3>Features</h3><p>Neque porro quisquam est qui dolorem ipsum quia dolor sit...</p><div class="more">Read more &gt;</div></div>
  <div class="feature" style="left:522px"><div class="tile" role="img" aria-label="Herb sprig icon" style="background:#f27060"></div><h3>Exhibitors</h3><p>Neque porro quisquam est qui dolorem ipsum quia dolor sit...</p><div class="more">Read more &gt;</div></div>
</section>

<div class="abs main"></div>
<h1 class="abs title">The Bright Plate &amp; Vine Fair 2012</h1>
<p class="abs intro">Lorem Ipsum is simply dummy text of the printing and typesetting industry. Lorem Ipsum has been the industry's standard dummy text ever since the 1500s, when an unknown printer took a galley of type and scrambled it to make a type specimen book.</p>
<svg class="abs calendar" width="38" height="34" viewBox="0 0 38 34" aria-hidden="true">
  <rect x="1" y="4" width="36" height="29" rx="3" fill="#eee" stroke="#999"/>
  <rect x="1" y="4" width="36" height="8" rx="3" fill="#777"/>
  <g fill="#bbb"><rect x="6" y="16" width="5" height="4"/><rect x="14" y="16" width="5" height="4"/><rect x="22" y="16" width="5" height="4"/><rect x="6" y="24" width="5" height="4"/><rect x="14" y="24" width="5" height="4"/><rect x="22" y="24" width="5" height="4"/></g>
</svg>
<p class="abs countdown">Sydney show starts in 14 weeks,<br>early bird tickets on sale now.</p>
<div class="abs early">GET EARLYBIRD TICKETS NOW</div>

<div class="abs tabs"><span class="on">Latest News</span><span>Highlights</span></div>
<div class="abs col news">
  <div class="item"><div class="item-title">Best in Show Wine Awards</div><p><span class="date">10 Jan 2012</span> There are many variations of passages of Lorem Ipsum available, but the majority have suffered alteration in some form.</p></div>
  <div class="item"><div class="item-title">New Chef announcements</div><p><span class="date">12 Jan 2012</span> There are many variations of passages of Lorem Ipsum available, but the majority have suffered alteration in some form.</p></div>
</div>
<div class="abs feed-head"><span>Chirper</span><span>#BrightPlate2012</span></div>
<div class="abs feed">
  <p><b>brightplate2012:</b> Cooking tonight? Make double and put next week's dinner on ice: <a>brpl.example/A0eEuJ</a></p>
  <p class="ago">7 hours ago</p>
  <p><b>brightplate2012:</b> Fancy yourself as the next big food writer? Here's our guide to writing a recipe. Let us know your hints and tips: <a>brpl.example/xHmS4J</a></p>
  <p class="ago">11 hours ago.</p>
</div>

<div class="abs ex-head">New Exhibitors in 2012</div>
<div class="exhibitor" style="top:720px"><div class="item-title">Highmeadow Berry Farm</div><p>The standard chunk of Lorem Ipsum used since the 1500s is reproduced below for those interested.</p><div class="pic" role="img" aria-label="Photo of a berry dessert" style="background:linear-gradient(135deg,#e8d9c0,#9a5a3a)"></div></div>
<div class="exhibitor" style="top:799px"><div class="item-title">Ridgefold Wines</div><p>The standard chunk of Lorem Ipsum used since the 1500s is reproduced below for those interested.</p><div class="pic" role="img" aria-label="Photo of stacked wine crates" style="background:linear-gradient(135deg,#9a8f86,#5e554f)"></div></div>
<div class="exhibitor" style="top:882px"><div class="item-title">Southland Avocado Oil</div><p>The standard chunk of Lorem Ipsum used since the 1500s is reproduced below for those interested.</p><div class="pic" role="img" aria-label="Photo of an oil bottle and halved avocado" style="background:linear-gradient(135deg,#fff,#d7c45a 60%,#6c8a2a)"></div></div>

<div class="abs ad ad-tall">Advertising<br>Placer</div>
<div class="abs ad ad-mid">Advertising<br>Placer</div>
<div class="abs ad ad-low">Advertising<br>Placer</div>

<footer>
  <div class="abs footer"></div>
  <div class="abs quick-head">Quicklinks</div>
  <div class="abs quick">
    <a>Home</a><a>About us</a><a>Location</a><a>Contact us</a><a>Tickets</a><a>Feedback</a><a>Blog</a><a>Terms of use</a><a>Sign up</a><a>Privacy policy</a><a>Exhibitors</a>
  </div>
  <div class="abs foot-dates">
    <h2>Bright Plate &amp; Vine Fair 2012 Dates</h2>
    <ul>
      <li><b>SYDNEY</b><span>22nd-24th June</span></li>
      <li><b>MELBOURNE</b><span>22nd-24th July</span></li>
      <li><b>PERTH</b><span>22nd-24th August</span></li>
      <li><b>BRISBANE</b><span>22nd-24th September</span></li>
    </ul>
  </div>
  <svg class="abs foot-tab" viewBox="0 0 112 112" aria-hidden="true">
    <polygon points="0,0 112,0 112,112 56,98 0,112" fill="#fff" stroke="#ccc"/>
  </svg>
  <div class="abs foot-name">Bright Plate &amp; Vine Fair</div>
  <p class="abs copyright">Copyright © 2012 Bright Plate &amp; Vine Fair. All Rights Reserved.</p>
</footer>
</body>
</html>
```